Business Card Design Project

We are an agricultural business based in Brisbane.
We design, manage and operate regional saleyards. Our logo is green/silver in colour and details of our business can be found on our website www.vodemarketyards.com.au

Just wanting a corporate design for some business cards and include name, position, contact details.

Thanks

Industry/Entity Type

Business

```html
<!DOCTYPE html>
<html lang="en">
<head>
<meta charset="utf-8">
<title>Vode Market Yards – Business Card</title>
<link href="https://fonts.googleapis.com/css2?family=PT+Sans:ital,wght@0,400;0,700;1,700&family=Montserrat:wght@700&display=swap" rel="stylesheet">
<style>
  :root {
    --page: #ffffff;
    --card-front: #f4f4f4;
    --card-back: #e5e6e7;
    --ink: #231f20;
    --green: #00843d;
    --silver: #939598;
  }
  * { margin: 0; padding: 0; box-sizing: border-box; }
  html, body { width: 1200px; height: 1000px; overflow: hidden; background: var(--page); }
  .canvas { position: relative; width: 1200px; height: 1000px; }
  .card { position: absolute; left: 253px; width: 697px; height: 418px; overflow: hidden; }
  .card--front { top: 60px; background: var(--card-front); }
  .card--back { top: 523px; background: var(--card-back); }

  .brand-name {
    font-family: "PT Sans", sans-serif;
    font-weight: 700;
    color: var(--ink);
    text-transform: uppercase;
    text-align: center;
    line-height: 1;
    letter-spacing: 0.01em;
  }
  .card--front .brand-name {
    position: absolute; left: 0; right: 0; top: 128px;
    font-size: 58px;
  }
  .card--front .brand-name span { display: block; margin-bottom: 8px; }
  .front-url {
    position: absolute; left: 0; right: 0; top: 292px;
    text-align: center;
    font-family: "PT Sans", sans-serif;
    font-size: 27px; color: var(--ink);
  }

  .card--back .brand-name {
    position: absolute; left: 46px; width: 302px; top: 76px;
    font-size: 34px;
  }
  .card--back .brand-name span { display: block; margin-bottom: 4px; }

  .person { position: absolute; right: 50px; top: 190px; text-align: right; }
  .person__name {
    font-family: "Montserrat", sans-serif; font-weight: 700;
    font-size: 25px; color: var(--green); letter-spacing: -0.01em; line-height: 1;
  }
  .person__role {
    margin-top: 6px;
    font-family: "PT Sans", sans-serif; font-style: italic; font-weight: 700;
    font-size: 15px; color: var(--ink);
  }
  .contacts { position: absolute; right: 50px; top: 250px; list-style: none; }
  .contacts li {
    display: flex; align-items: center; height: 25.5px; white-space: nowrap;
    font-family: "PT Sans", sans-serif; font-weight: 700; font-size: 14px; color: var(--green);
  }
  .contacts svg { width: 14px; height: 14px; margin-right: 12px; flex: none; }

  .band-silver { position: absolute; left: 0; right: 0; top: 356px; height: 9px; background: var(--silver); }
  .band-green { position: absolute; left: 0; right: 0; top: 365px; bottom: 0; background: var(--green); }
</style>
</head>
<body>
<div class="canvas">
  <section class="card card--front">
    <h1 class="brand-name"><span>Vode Market</span><span>Yards</span></h1>
    <p class="front-url">www.vodemarketyards.com.au</p>
  </section>

  <section class="card card--back">
    <p class="brand-name"><span>Vode Market</span><span>Yards</span></p>
    <div class="person">
      <p class="person__name">DANIEL HARWOOD</p>
      <p class="person__role">General Manager</p>
    </div>
    <ul class="contacts">
      <li>
        <svg viewBox="0 0 14 14" aria-hidden="true"><path d="M4 1h3l-1 3-1.5 1c.6 1.8 1.7 3 3.5 3.8L9 7.5l3 1v3c-6 .5-9.5-4-8-10.5z" fill="var(--ink)"/></svg>
        +0400.555.217
      </li>
      <li>
        <svg viewBox="0 0 14 14" aria-hidden="true"><circle cx="7" cy="7" r="6" fill="none" stroke="var(--ink)" stroke-width="1.6"/><path d="M3 5c2 0 2 2 4 2s1 3 0 5M9 2c0 2 2 2 3 3" fill="none" stroke="var(--ink)" stroke-width="1.4"/></svg>
        www.vodemarketyards.com.au
      </li>
      <li>
        <svg viewBox="0 0 14 14" aria-hidden="true"><rect x="1" y="3" width="12" height="8" fill="none" stroke="var(--ink)" stroke-width="1.4"/><path d="M1 3l6 5 6-5M1 11l4.5-4M13 11L8.5 7" fill="none" stroke="var(--ink)" stroke-width="1.2"/></svg>
        daniel@vodemarketyards.com.au
      </li>
    </ul>
    <div class="band-silver"></div>
    <div class="band-green"></div>
  </section>
</div>
</body>
</html>
```